依頼詳細
富山県高岡市「緑ヶ丘市議会」で、明協系会派「明政協和党緑ヶ丘市議会議員会」を結成し、活動を行ってきましたが、それを市民の皆さんにお伝えするために、会報誌を発行したくコンペ方式でデザインをお願いするものです。
宜しくお願い致します。
記載項目
明政協和党緑ヶ丘市議会議員会/090-2846-3917(政調会長森下)/作成料5~10万円
サイズ
B4
ページ数
両面
希望イメージ
シンプル 複雑
単色 カラフル
暗い 明るい
日常 高級
遊び心 厳粛
未来的 伝統的
女性的 男性的
希望する色
赤系、緑系、黄・オレンジ系
納品ファイル
• イラストレーター形式 (.ai)
補足説明
・非常に急いでいます
・ロゴは下記からダウンロードお願いします(ただし、党の広報誌でなく、議会会派の広報誌なので控えめでお願いします)
https://www.sakura-meikyo.jp/policy-koho
https://www.sakura-meikyo.jp/introduction2/pdf/logo_type_A.JPG
デザイン案の提示を使用にも情報が不足しているとのご指摘・ご質問を頂きました。

そこで、掲載する内容(タイトル、文章、写真及びキャプション)を1つのWordデータにまとめました。
また、当方において、手書きで記載したレイアウト案図(表面及び裏面)データ2点を合わせて送付します。

なお、デザインの良さと価格を見て採用を決めたいと思いますので、
その点も踏まえてご提案を宜しくお願いします。
本件は12月10日(木)に開始するも、情報が不足しているとのご意見・ご指摘を受けました。
そこで、12月13日(日)夜中に、掲載頂きたい情報(文章や写真及びキャプションなど)を追記したところです。

今般、当該内容について、少しだけ修正を加えました。
修正箇所は分かりやすいように黄色に着色又は黄色の枠で囲ってありますので、ご確認の上、既に提出の方は修正対応頂ければ幸いに存じます。
未提出の方は、今回のデータを元にデザイン案を作成願います。

なお、仮に修正対応されなかったとしても、レイアウトの案をご提示いただいていますので、それでもって、私たちの会派の政務調査会を開催し、採用デザイン案を週明け12月22日(月)に決定する予定です。

以上、宜しくお願い致します。
■ 選んだ理由

シンプルで明瞭なデザイン、色使いで、パッと見て目につきやすい印象を受けました。
今回の私たちの目的が、多くの市民の皆さまにご覧頂くことであり、その観点から一番最適であると判断した次第です。

■ 提案者全員のお礼・コメント

年末の依頼で、皆さまお忙しい中、多くのご提案を頂きました。
そして提案のどれもが、非常に質が高く、驚きと感動をもって全提案を拝見させて頂きました。
残念ながら、選定できるのは1点であり、選定できなかった皆さま方には誠に申し訳ございません。

なお、今回初の会派広報紙の発行、そしてクリエモールの活用であり、今後もし仕事を依頼することがありましたら、その際にはぜひご協力頂ければ幸いに存じます。

皆さまのご健康とご多幸、そして良い年を迎えられるよう祈念申し上げ御礼のコメントとします。
誠にありがとうございました。

```html
<!DOCTYPE html>
<html lang="ja">
<head>
<meta charset="utf-8">
<title>会派だより 明政協和党緑ヶ丘市議会議員会</title>
<link rel="stylesheet" href="https://fonts.googleapis.com/css2?family=Noto+Sans+JP:wght@400;500;700;900&family=Zen+Maru+Gothic:wght@700;900&display=swap">
<style>
:root{
  --green:#2e8b3d;
  --green-dark:#1f6b2c;
  --green-pale:#e6f2dd;
  --red:#d7261e;
  --yellow:#f6d31c;
  --yellow-pale:#fff7cf;
  --ink:#222;
  --muted:#666;
  --rule:#bcd9b2;
  --photo-a:#8c9a8e;
  --photo-b:#b9c2b6;
  --sky:#a9c8e4;
  --snow:#e9eef2;
}
*{box-sizing:border-box;margin:0;padding:0}
html,body{width:846px;height:1200px;overflow:hidden;background:#fff}
body{font-family:"Noto Sans JP",sans-serif;color:var(--ink);position:relative;font-size:9.5px;line-height:1.6}
.abs{position:absolute}
.masthead{left:18px;top:12px;width:330px;height:80px;border:2px solid var(--green);border-radius:8px;padding:6px 12px;display:flex;align-items:center}
.masthead h1{font-family:"Zen Maru Gothic",sans-serif;font-weight:900;color:var(--green);font-size:24px;line-height:1.3;letter-spacing:1px}
.masthead h1 .num{color:var(--red);font-size:28px}
.org-name{right:22px;top:40px;font-weight:700;font-size:13px;color:var(--green-dark);letter-spacing:1px}
.head-rule{left:0;top:98px;width:846px;height:5px;background:var(--green)}
.topic-title{display:flex;gap:7px;align-items:flex-start;font-family:"Zen Maru Gothic",sans-serif;font-weight:900;font-size:17px;line-height:1.3;color:var(--green-dark)}
.topic-title em{font-style:normal;color:var(--red)}
.badge{flex:none;width:24px;height:24px;border-radius:50%;background:var(--green);color:#fff;font-size:15px;display:flex;align-items:center;justify-content:center;margin-top:1px}
.topic p{margin-top:8px;text-indent:1em;text-align:justify}
.photo{background:linear-gradient(135deg,var(--photo-a),var(--photo-b));border:1px solid #999}
.caption{font-size:8px;color:var(--muted);margin-top:3px}
.topic4{left:18px;top:112px;width:400px}
.topic5{left:432px;top:112px;width:396px}
.divider{left:425px;top:112px;width:1px;height:330px;background:var(--rule)}
.band6{left:18px;top:450px;width:810px;height:30px;background:var(--green-pale);border-left:6px solid var(--green);display:flex;align-items:center;padding-left:8px}
.col{width:395px}
.col h3{font-size:11px;font-weight:700;color:var(--green-dark);border-bottom:1px solid var(--rule);margin-bottom:4px}
.col p{text-indent:1em;text-align:justify}
.col6a{left:18px;top:488px}
.col6b{left:433px;top:488px}
.mountains{left:433px;top:615px;width:395px;height:78px;background:linear-gradient(180deg,var(--sky) 0%,var(--snow) 60%,var(--photo-b) 100%);border:1px solid #999}
.note{left:18px;top:700px;width:810px;height:46px;border:1.5px solid var(--yellow);background:var(--yellow-pale);padding:5px 10px;font-size:9px;line-height:1.55}
.note b{color:var(--red)}
.stats-head{left:18px;top:758px;width:200px;height:82px;background:var(--green-pale);border-radius:6px;padding:8px 14px;font-family:"Zen Maru Gothic",sans-serif;font-weight:900}
.stats-head .l1{color:var(--red);font-size:27px;line-height:1.1}
.stats-head .l2{color:var(--green-dark);font-size:27px;line-height:1.2}
.stats-lead{left:232px;top:764px;width:596px;font-size:9.5px;line-height:1.7}
.stats-lead .hl{color:var(--red);font-weight:700}
.stat-table{left:18px;top:856px;width:395px;border-collapse:collapse}
.stat-table td{border:1px solid var(--green);padding:0 8px;height:38px;font-size:10px}
.stat-table td.n{text-align:right;width:70px;font-weight:900;font-size:13px;color:var(--red)}
.stat-table td.n small{font-size:9px;color:var(--ink);font-weight:500}
.stat-table tr:nth-child(odd) td{background:#f6fbf3}
.roles{left:433px;top:856px;width:395px;border:1px solid var(--green)}
.roles .row{display:flex;justify-content:space-between;align-items:center;padding:0 8px;height:38px;background:#f6fbf3;border-bottom:1px solid var(--green);font-size:10px}
.roles .row strong{color:var(--red);font-size:13px;font-weight:900}
.roles .list{padding:6px 9px;font-size:8.5px;line-height:1.65;height:245px;overflow:hidden}
.roles .list li{list-style:none}
.stat-note{left:18px;top:1020px;width:395px;font-size:8.5px;color:var(--muted);line-height:1.6}
.footer{left:0;top:1176px;width:846px;height:24px;background:var(--green);color:#fff;font-size:9px;display:flex;align-items:center;justify-content:center;gap:16px}
</style>
</head>
<body>

<header class="abs masthead">
  <h1>私たちが議会で質問した<br>数は<span class="num">298</span>項目に遡る</h1>
</header>
<div class="abs org-name">明政協和党緑ヶ丘市議会議員会</div>
<div class="abs head-rule"></div>

<section class="abs topic topic4">
  <div class="topic-title"><span class="badge">4</span><span>議会改革断行、公正な議会へ！不適切な<br>政務活動費の使用問題に、<em>厳正に対処!!</em></span></div>
  <p>市議会の会派「明政協和党緑ヶ丘市議会議員会」が令和元年度、政務活動費の不適切な使用問題を調査し、平成28年度から令和元年度までの4年間で計約200万円の返還を行いました。これは市民の皆さまの信頼を大きく損なうものであり、深くお詫び申し上げます。</p>
  <p>会派では再発防止に向け、支出基準の見直しや領収書の公開、第三者によるチェック体制の導入など、透明性の高い議会運営に取り組んでいます。今後も公正な議会を目指してまいります。</p>
  <div class="photo" role="img" aria-label="会派会議で政務活動費の再発防止策を協議する議員の写真" style="width:400px;height:128px;margin-top:10px"></div>
  <div class="caption">再発防止策について協議する会派会議の様子</div>
</section>

<div class="abs divider"></div>

<section class="abs topic topic5">
  <div class="topic-title"><span class="badge">5</span><span>政策集団として、政策立案に向け、年間通じて<em>研修会や政調会を開催！</em></span></div>
  <div style="display:flex;gap:10px;margin-top:8px">
    <p style="margin-top:0;flex:1">会派の政策立案力を高めるため、外部講師を招いた研修会や、各分野の政務調査会を年間通じて開催しています。地域の声を政策に反映させるため、各種団体との意見交換会も積極的に行っています。</p>
    <div><div class="photo" role="img" aria-label="政調会の会議風景の写真" style="width:150px;height:92px"></div><div class="caption">政調会の会議風景</div></div>
  </div>
  <div style="display:flex;gap:10px;margin-top:6px">
    <div style="flex:1"><div class="photo" role="img" aria-label="外部講師を招いた研修会の写真" style="width:100%;height:128px"></div><div class="caption">外部講師による研修会</div></div>
    <div style="flex:1"><div class="photo" role="img" aria-label="団体との意見交換会の写真" style="width:100%;height:128px"></div><div class="caption">各種団体との意見交換会</div></div>
  </div>
</section>

<div class="abs band6"><div class="topic-title"><span class="badge">6</span><span>政策提言！本会議<em>「会派代表質問」</em>を通じ、市政を発展！</span></div></div>

<section class="abs col col6a">
  <h3>① 会派代表質問とは</h3>
  <p>会派代表質問は、年4回の定例会のうち、当初予算を審議する3月議会で行われる質問です。会派を代表して市長の施政方針や予算案について質問し、会派としての考えや政策提言を市政に届ける重要な機会です。</p>
  <p>質問時間は会派の人数に応じて配分され、当会派は最大会派として最も長い時間を確保しています。一問一答方式を取り入れた「緑ヶ丘式質問」により、論点を明確にした議論を行っています。</p>
  <p>市民生活に直結する子育て、教育、防災、地域経済などの幅広い分野について、現場の声をもとに具体的な提案を重ねてきました。</p>
</section>

<section class="abs col col6b">
  <h3>② これまでの代表質問について</h3>
  <p>令和元年までの代表質問では、新庁舎整備、中心市街地の活性化、人口減少対策、公共交通の維持など、市の将来を左右する課題を取り上げ、市当局から前向きな答弁を引き出してきました。</p>
</section>
<div class="abs mountains" role="img" aria-label="雪をいただいた連峰と市街地の風景写真"></div>

<div class="abs note">上記①のとおり、会派代表質問は市政の方向性を左右する重要な場です。<b>当会派の提言が予算に反映された事業</b>は、子育て支援の拡充や防災体制の強化など多岐にわたります。<br>詳細は会派の活動報告資料（市議会ホームページ掲載）をご覧ください。</div>

<div class="abs stats-head"><div class="l1">数字で見る</div><div class="l2">私たちの活動</div></div>
<p class="abs stats-lead">上記に加え、会派所属議員は本会議での一般質問や予算要望を通じて、市民の皆さまの声を市政に届けてきました。<span class="hl">4年間の活動を数字でご紹介します。</span>これからも市民の皆さまに身近な議会を目指し、一つ一つの声を大切にしてまいります。数字は令和2年11月末時点のものです。</p>

<table class="abs stat-table">
  <tr><td>議会「一般質問」での延べ登壇回数（※）</td><td class="n">38<small>回</small></td></tr>
  <tr><td>議会「一般質問」での延べ質問項目数</td><td class="n">497<small>件</small></td></tr>
  <tr><td>令和2年度予算に対する要望件数</td><td class="n">139<small>件</small></td></tr>
  <tr><td>令和3年度予算に対する要望件数</td><td class="n">144<small>件</small></td></tr>
</table>
<p class="abs stat-note">※ 平成29年11月から令和2年11月までの集計です。会派代表質問を含みます。</p>

<div class="abs roles">
  <div class="row"><span>当会派で担っている主な議会役職員数（※）</span><strong>58</strong></div>
  <ul class="list">
    <li>議長・副議長／監査委員／議会運営委員長</li>
    <li>総務文教常任委員長／民生病院常任委員長</li>
    <li>産業建設常任委員長／予算特別委員長</li>
    <li>決算特別委員長／新庁舎整備特別委員長</li>
    <li>まちづくり特別委員長／防災対策特別委員長</li>
    <li>広域連合議会議員／一部事務組合議会議員</li>
    <li>各種審議会委員／都市計画審議会委員</li>
    <li>農業委員会委員／国民健康保険運営協議会委員</li>
    <li>※役職は延べ人数で集計しています。</li>
  </ul>
</div>

<footer class="abs footer"><span>発行：明政協和党緑ヶ丘市議会議員会</span><span>連絡先：090-2846-3917（政調会長 森下）</span></footer>

</body>
</html>
```